Book Cover for Memoir: Sexual Assault and Traumatic Stress

I need a cover design for a memoir that is a victim's story of a sexual assault. I will need a print-on-demand cover, an eBook cover, and a 3D thumbnail image. The thumbnail and eBook cover will be used immediately, and the POD cover will be used in a few months with the full manuscript is ready. Therefore, I need an artist who is willing to make small adjustments if needed once the page count is set.

I have a image I have purchased that should give you an idea of the desired direction, but you can feel free to use your own images. I have attached some examples of book covers I like. I attached a color palette for fonts.

Overall Look: Fonts should be feminine and thin, but large to stand out. Look should be simple and elegant, and display and overall depressing feeling. There should be enough detail though to make it look professionally put together. Not TOO minimalistic.

I have also attached the Print Harbor templates if you choose to use those. If not, ensure there is an open place for the barcode on the bottom right.

Requirements
Must have
• Title: Beneath Quiet Rain
Subtitle: One Woman's Account of Fear, Guilt & Silence
Author: Dana Ruth Whitford
Audience: Mostly women 18-30
Quote (for the back): "I always thought I'd know how I'd react if I ever was raped. I was wrong. I've been wrong a lot lately."
Summary (back cover): When twenty-seven-year-old Dana Whitford wakes up with a gut-wrenching feeling, she has little memory of the horrifying events that occurred the night before. Days earlier, Dana was a spirited single mom who had abandoned her hometown to raise her daughter in the city and pursue her dreams. In the short months since Dana’s move to Seattle, she became the adored lover of a charismatic lawyer, started a new business, and finally felt life was going her way. So what happened to cause her to break?

In a gripping and heartbreaking narrative, Dana tells the true story of how her life unraveled from the traumatic events that took place that night and why what seems obvious to everyone else is impossible for Dana to believe. Beneath Quiet Rain is a chilling exploration of memory through trauma, trust in humanity, and a captivating story of strength and survival that appeals to the heart of fathers and mothers, sons and daughters, and men and women alike.
Nice to have
• BACK COVER: I'd like to have a photo on the back. This should depict the happy life of the main character before the sexual assault, and should be with her daughter. Or should be a nature scene that starts at the corner and blends into the rest of the cover. I have attached a possible image or you can use something you like.

```html
<!DOCTYPE html>
<html lang="en">
<head>
<meta charset="utf-8">
<title>Beneath Quiet Rain — Cover with Spine</title>
<link rel="stylesheet" href="https://fonts.googleapis.com/css2?family=Pinyon+Script&family=Arimo:ital,wght@0,400;1,400&display=swap">
<style>
  :root {
    --stage: #efefef;
    --cover: #343434;
    --spine: #2c2c2c;
    --cover-edge: #262626;
    --title-red: #b5303a;
    --title-glow: #e07a80;
    --author-grey: #d6d6d6;
    --tagline-red: #c23a3f;
    --photo-cool: #9fb0c6;
    --photo-mid: #cfd3db;
    --photo-warm: #ece4df;
    --paper-edge: #f4f2f0;
  }
  * { margin: 0; padding: 0; box-sizing: border-box; }
  html, body {
    width: 1200px;
    height: 800px;
    overflow: hidden;
    background: var(--stage);
  }
  .stage {
    width: 1200px;
    height: 800px;
    display: flex;
    align-items: center;
    justify-content: center;
  }
  .book {
    display: flex;
    height: 740px;
  }

  /* Spine */
  .spine {
    position: relative;
    width: 96px;
    height: 100%;
    background: var(--spine);
    box-shadow: inset -1px 0 0 var(--cover-edge), inset 0 0 0 1px var(--cover-edge);
  }
  .spine-title {
    position: absolute;
    top: 40px;
    left: 0;
    width: 100%;
    height: 400px;
    display: flex;
    justify-content: center;
    writing-mode: vertical-rl;
    font-family: "Pinyon Script", cursive;
    font-weight: 400;
    font-size: 46px;
    line-height: 96px;
    color: var(--title-red);
    -webkit-text-stroke: 0.5px var(--title-glow);
    white-space: nowrap;
  }
  .spine-author {
    position: absolute;
    top: 500px;
    left: 0;
    width: 100%;
    display: flex;
    justify-content: center;
    writing-mode: vertical-rl;
    font-family: "Arimo", sans-serif;
    font-weight: 400;
    font-size: 24px;
    line-height: 28px;
    color: var(--author-grey);
    white-space: nowrap;
  }

  /* Front cover */
  .front-cover {
    position: relative;
    width: 510px;
    height: 100%;
    background: var(--cover);
    box-shadow: inset 0 0 0 1px var(--cover-edge);
  }
  .book-title {
    position: absolute;
    top: 48px;
    left: 0;
    width: 100%;
    text-align: center;
    font-family: "Pinyon Script", cursive;
    font-weight: 400;
    font-size: 58px;
    line-height: 1;
    color: var(--title-red);
    -webkit-text-stroke: 0.6px var(--title-glow);
    white-space: nowrap;
  }
  .cover-photo {
    position: absolute;
    top: 168px;
    left: 95px;
    width: 290px;
    height: 380px;
  }
  .author-name {
    position: absolute;
    top: 578px;
    left: 0;
    width: 100%;
    text-align: center;
    font-family: "Arimo", sans-serif;
    font-weight: 400;
    font-size: 35px;
    letter-spacing: 0.5px;
    color: var(--author-grey);
  }
  .tagline {
    position: absolute;
    top: 640px;
    left: 0;
    width: 100%;
    text-align: center;
    font-family: "Arimo", sans-serif;
    font-style: italic;
    font-size: 15.5px;
    letter-spacing: 0.3px;
    color: var(--tagline-red);
  }
</style>
</head>
<body>
  <main class="stage">
    <div class="book">
      <aside class="spine">
        <p class="spine-title">Beneath Quiet Rain</p>
        <p class="spine-author">Dana<br>Ruth Whitford</p>
      </aside>

      <section class="front-cover">
        <h1 class="book-title">Beneath Quiet Rain</h1>

        <svg class="cover-photo" viewBox="0 0 290 380" role="img"
             aria-label="Torn portrait photograph of a pale young woman with dark hair in a white dress, split in two pieces">
          <defs>
            <linearGradient id="photo-tone" x1="0" y1="0" x2="0" y2="380" gradientUnits="userSpaceOnUse">
              <stop offset="0" stop-color="#9fb0c6"/>
              <stop offset="0.45" stop-color="#cfd3db"/>
              <stop offset="1" stop-color="#ece4df"/>
            </linearGradient>
          </defs>
          <polygon class="photo-piece photo-piece--upper"
                   fill="url(#photo-tone)" stroke="#f4f2f0" stroke-width="2"
                   points="0,0 290,0 290,186 262,196 232,182 204,194 176,176 146,190 118,172 88,184 58,166 30,176 0,164"/>
          <polygon class="photo-piece photo-piece--lower"
                   fill="url(#photo-tone)" stroke="#f4f2f0" stroke-width="2"
                   points="0,180 30,192 58,182 88,200 118,188 146,206 176,192 204,210 232,198 262,212 290,202 290,380 0,380"/>
        </svg>

        <p class="author-name">Dana Ruth Whitford</p>
        <p class="tagline">...one woman's account of fear, guilt &amp; silence</p>
      </section>
    </div>
  </main>
</body>
</html>
```